Business card design needed

I need a business card for my new business.
I make environmentally friendly candles from all natural premium ingredients.
The candles are hand-poured locally in Melbourne, Australia.
I also want my card to match my website www.velmirawicks.com.au (similar colours, font). Can add additional fonts to create more interest...
I want my design to reflect class and simplicity.
Target Market(s)
Target audience 25-50
The candles represent luxury but need to appeal to the environmentally conscious...
Needs to appeal to both men and women. A luxury gift a man would buy for his girlfriend or mother or for his home and for a woman it needs to represent quality...
Industry/Entity Type
Business
Contact Information for Business Card
Velmira Candles
Hand-Poured Eco Soy Candles
Lorraine Quibell - Founder
0438 276 904
www.velmirawicks.com.au
Logo Text
VELMIRA
Logo styles of interest
Wordmark Logo
Look and feel
Each slider illustrates characteristics of the customer's brand and the style your logo design should communicate.

```html
<!DOCTYPE html>
<html lang="en">
<head>
<meta charset="utf-8">
<title>Velmira Candles – Business Card</title>
<link rel="stylesheet" href="https://fonts.googleapis.com/css2?family=Crimson+Text:wght@400&family=Didact+Gothic&display=swap">
<style>
  :root {
    --canvas-bg: #ecebe8;
    --card-white: #ffffff;
    --card-blue-top: #d7ecef;
    --card-blue-bottom: #bddde3;
    --ink-brand: #4a4a4a;
    --ink-tagline: #3d3d3d;
    --ink-body: #1f2426;
    --frame-line: #2b3033;
  }
  * { box-sizing: border-box; margin: 0; padding: 0; }
  html, body {
    width: 1200px;
    height: 1000px;
    overflow: hidden;
    background: var(--canvas-bg);
  }
  .canvas {
    position: relative;
    width: 1200px;
    height: 1000px;
  }
  .business-card {
    position: absolute;
    left: 150px;
    top: 225px;
    width: 900px;
    height: 550px;
    background: linear-gradient(180deg, var(--card-blue-top) 0%, var(--card-blue-bottom) 100%);
    box-shadow: 0 6px 24px rgba(0,0,0,0.12);
    overflow: hidden;
  }
  .brand-band {
    position: absolute;
    left: 0; top: 0;
    width: 100%;
    height: 160px;
    background: var(--card-white);
    text-align: center;
    padding-top: 38px;
  }
  .brand-name {
    font-family: "Crimson Text", serif;
    font-weight: 400;
    font-size: 44px;
    color: var(--ink-brand);
    line-height: 1;
  }
  .brand-tagline {
    font-family: "Crimson Text", serif;
    font-size: 25px;
    color: var(--ink-tagline);
    margin-top: 8px;
  }
  .person {
    position: absolute;
    left: 62px;
    top: 205px;
    font-family: "Didact Gothic", sans-serif;
    color: var(--ink-body);
  }
  .person-name {
    font-size: 46px;
    letter-spacing: 0.03em;
    word-spacing: 0.25em;
    line-height: 1;
  }
  .person-role {
    font-size: 26px;
    margin-top: 2px;
    letter-spacing: 0.03em;
  }
  .contact-frame {
    position: absolute;
    left: 440px;
    top: 265px;
    width: 410px;
    height: 180px;
    border: 1.5px solid var(--frame-line);
    display: flex;
    flex-direction: column;
    justify-content: center;
    align-items: center;
    gap: 22px;
    font-family: "Didact Gothic", sans-serif;
    color: var(--ink-body);
  }
  .contact-phone {
    font-size: 27px;
    letter-spacing: 0.12em;
  }
  .contact-web {
    font-size: 25px;
    letter-spacing: 0.05em;
  }
</style>
</head>
<body>
  <main class="canvas">
    <section class="business-card">
      <header class="brand-band">
        <h1 class="brand-name">Velmira Candles</h1>
        <p class="brand-tagline">Hand-Poured Eco Soy Candles</p>
      </header>
      <div class="person">
        <p class="person-name">Lorraine Quibell</p>
        <p class="person-role">Founder</p>
      </div>
      <div class="contact-frame">
        <p class="contact-phone">Ph: 0438 276 904</p>
        <p class="contact-web">www.velmirawicks.com.au</p>
      </div>
    </section>
  </main>
</body>
</html>
```